Colin Dwyer Moving DL Flyer

We need a double sided DL flyer to give to patients to let them know that we are moving location.
On one side we would like it to read:
"We Are Moving!" and "November 2017" and our logo.
On the other side we would like it to read:
"Same Great Staff"
"Same Great Service"
"Bigger, Brighter and Better"
"New Location at 52 Fernlow St"
with a map below (attached)
The flyer should follow our practice branding. Attached is a copy of our business card as an example of this.

```html
<!DOCTYPE html>
<html lang="en">
<head>
<meta charset="utf-8">
<title>Colin Dwyer Optometry – Moving DL Flyer</title>
<link rel="stylesheet" href="https://fonts.googleapis.com/css2?family=Open+Sans:wdth,wght@75..100,300..800&display=swap">
<style>
  :root {
    --board: #474747;
    --paper: #ffffff;
    --plum: #4a3853;
    --plum-deep: #3e2e47;
    --grey: #a3a3a3;
    --ink: #222222;
    --label: #ffffff;
    --bracket: #c8c8c8;
  }
  * { margin: 0; padding: 0; box-sizing: border-box; }
  html, body {
    width: 1200px; height: 850px; overflow: hidden;
    background: var(--board);
    font-family: "Open Sans", Arial, sans-serif;
  }
  .board { position: relative; width: 1200px; height: 850px; }

  .flyer {
    position: absolute; top: 73px; width: 334px; height: 667px;
    background: var(--paper);
    box-shadow: 6px 10px 18px rgba(0,0,0,.45);
    overflow: hidden;
  }
  .flyer--front { left: 213px; }
  .flyer--back { left: 633px; }

  .side-label {
    position: absolute; top: 768px; width: 334px; text-align: center;
    color: var(--label); font-size: 32px; font-weight: 400;
  }
  .side-label--front { left: 205px; }
  .side-label--back { left: 633px; }

  /* Brand lockup */
  .brand { position: absolute; display: flex; align-items: flex-start; }
  .brand__mark { background: var(--ink); flex: none; }
  .brand__name { color: var(--ink); font-weight: 400; line-height: 1; }
  .brand__name span { display: block; }
  .brand__tagline { color: var(--plum); font-weight: 400; }

  .flyer--front .brand { left: 34px; top: 26px; }
  .flyer--front .brand__mark { width: 38px; height: 38px; margin: 18px 36px 0 0; }
  .flyer--front .brand__first { font-size: 21px; letter-spacing: -.2px; }
  .flyer--front .brand__second { font-size: 40px; letter-spacing: -.8px; margin-top: 2px; }
  .flyer--front .brand__tagline { font-size: 14.5px; margin-top: 8px; }

  .flyer--back .brand { left: 76px; top: 22px; }
  .flyer--back .brand__mark { width: 28px; height: 28px; margin: 14px 22px 0 0; }
  .flyer--back .brand__first { font-size: 15px; }
  .flyer--back .brand__second { font-size: 27px; letter-spacing: -.5px; margin-top: 1px; }
  .flyer--back .brand__tagline { font-size: 11px; margin-top: 5px; }

  /* Front */
  .hero { position: absolute; left: 0; top: 130px; width: 334px; height: 330px; }

  .headline {
    position: absolute; left: 36px; top: 461px;
    color: var(--plum); font-stretch: 75%; font-weight: 700;
    display: flex; align-items: flex-end; line-height: .85;
  }
  .headline__we { font-size: 66px; margin-right: 6px; }
  .headline__stack span { display: block; }
  .headline__are { font-size: 32px; }
  .headline__moving { font-size: 56px; }

  .move-date {
    position: absolute; left: 0; width: 334px; top: 560px; text-align: center;
    font-stretch: 75%; font-weight: 700; font-size: 43px; line-height: 1;
  }
  .move-date__month { color: var(--grey); }
  .move-date__year { color: var(--ink); }

  .web {
    position: absolute; left: 10px; right: 10px; top: 627px;
    display: flex; align-items: center; gap: 14px;
    font-stretch: 75%; font-weight: 700; font-size: 21px; color: var(--ink);
  }
  .web::before, .web::after { content: ""; flex: 1; height: 1px; background: var(--ink); }
  .flyer--back .web::before, .flyer--back .web::after { background: var(--plum); height: 2px; }

  /* Back */
  .map-frame { position: absolute; left: 47px; top: 99px; width: 240px; height: 226px; }
  .map-frame::before, .map-frame::after {
    content: ""; position: absolute; top: 0; width: 14px; height: 226px;
    border: 7px solid var(--bracket);
  }
  .map-frame::before { left: 0; border-right: none; }
  .map-frame::after { right: 0; border-left: none; }
  .map {
    position: absolute; left: 28px; top: 25px; width: 180px; height: 173px;
    background: linear-gradient(135deg, #3a3a3a 0%, #cfcfcf 35%, #f4a3a1 65%, #3a3a3a 100%);
  }

  .promise {
    position: absolute; top: 347px; width: 146px; height: 70px;
    background: var(--plum); border-radius: 8px;
    box-shadow: 0 4px 5px rgba(0,0,0,.35);
    color: #fff; text-align: center; font-stretch: 75%;
    font-size: 28px; line-height: 1; padding-top: 7px;
  }
  .promise span { display: block; }
  .promise__lead { font-weight: 400; }
  .promise__key { font-weight: 700; margin-top: 2px; }
  .promise--service { left: 12px; }
  .promise--staff { left: 177px; }

  .claim {
    position: absolute; left: 0; width: 334px; top: 433px; text-align: center;
    color: var(--plum); font-stretch: 75%; font-weight: 700; font-size: 35px; line-height: 1;
  }
  .claim span { display: block; }
  .claim__and { color: var(--grey); }

  .location-tag {
    position: absolute; left: 85px; top: 525px; width: 164px; height: 24px;
    background: var(--plum); border-radius: 6px;
    box-shadow: 0 4px 5px rgba(0,0,0,.3);
    color: #fff; text-align: center; font-size: 16px; font-weight: 300; line-height: 24px;
  }
  .pin { position: absolute; left: 155px; top: 563px; }
  .address {
    position: absolute; left: 90px; top: 578px; width: 155px; height: 40px;
    border: 1.5px solid #666; background: var(--paper);
    color: var(--plum-deep); text-align: center;
    font-stretch: 75%; font-weight: 700; font-size: 21px; line-height: 37px;
  }
</style>
</head>
<body>
<div class="board">

  <section class="flyer flyer--front">
    <div class="brand">
      <div class="brand__mark"></div>
      <div>
        <p class="brand__name"><span class="brand__first">Colin Dwyer</span><span class="brand__second">Optometry</span></p>
        <p class="brand__tagline">See Better. See Us.</p>
      </div>
    </div>

    <svg class="hero" viewBox="0 0 334 330" aria-hidden="false">
      <defs>
        <linearGradient id="exam-tones" x1="0" y1="0" x2="1" y2="1">
          <stop offset="0" stop-color="#e7b79c"/>
          <stop offset=".45" stop-color="#f2e2d8"/>
          <stop offset=".75" stop-color="#d8c3b1"/>
          <stop offset="1" stop-color="#b9a08a"/>
        </linearGradient>
      </defs>
      <ellipse cx="170" cy="172" rx="245" ry="142" transform="rotate(-22 170 172)" fill="var(--plum)"/>
      <ellipse cx="168" cy="170" rx="240" ry="130" transform="rotate(-17 168 170)" fill="url(#exam-tones)"
               role="img" aria-label="Photo of an optometrist examining an older patient at an eye testing machine"/>
    </svg>

    <h1 class="headline">
      <span class="headline__we">WE</span>
      <span class="headline__stack"><span class="headline__are">ARE</span><span class="headline__moving">MOVING!</span></span>
    </h1>
    <p class="move-date"><span class="move-date__month">NOVEMBER</span> <span class="move-date__year">2017</span></p>
    <p class="web">www.colindwyer.com.au</p>
  </section>

  <section class="flyer flyer--back">
    <div class="brand">
      <div class="brand__mark"></div>
      <div>
        <p class="brand__name"><span class="brand__first">Colin Dwyer</span><span class="brand__second">Optometry</span></p>
        <p class="brand__tagline">See Better. See Us.</p>
      </div>
    </div>

    <div class="map-frame">
      <div class="map" role="img" aria-label="Street map showing the new practice location beside the marketplace, near the laneway and car parking"></div>
    </div>

    <p class="promise promise--service"><span class="promise__lead">SAME GREAT</span><span class="promise__key">SERVICE</span></p>
    <p class="promise promise--staff"><span class="promise__lead">SAME GREAT</span><span class="promise__key">STAFF</span></p>

    <h2 class="claim"><span>BIGGER, BRIGHTER</span><span><span class="claim__and" style="display:inline">AND</span> BETTER</span></h2>

    <p class="location-tag">NEW LOCATION</p>
    <svg class="pin" width="24" height="24" viewBox="0 0 24 24" aria-hidden="true">
      <circle cx="12" cy="12" r="11" fill="#fff" stroke="#333" stroke-width="1.5"/>
      <path d="M12 5.5a4 4 0 0 0-4 4c0 3 4 7.5 4 7.5s4-4.5 4-7.5a4 4 0 0 0-4-4z" fill="#222"/>
      <circle cx="12" cy="9.5" r="1.5" fill="#fff"/>
    </svg>
    <p class="address">52 FERNLOW ST</p>

    <p class="web">www.colindwyer.com.au</p>
  </section>

  <p class="side-label side-label--front">Front</p>
  <p class="side-label side-label--back">Back</p>

</div>
</body>
</html>
```